Equipment Supplier Brochure Needed

We need a professional one-page, front-and-back brochure for Tovrik, an equipment and parts supplier serving peanut shelling and processing facilities across the Southeast. This brochure will be used as a leave-behind with plant managers and procurement teams, so it must look clean, modern, and visually strong.

Front of brochure:

Tovrik logo and strong branding

Brief headline/summary of what Tovrik does

Product category overview listed on the front (high-level, clean layout)

Flat Screens (slot, round, herringbone, square, Style 1 & Style 2)

Sheller Grates

Ripple Screens

Sheller Bars

Eccentric Bearing Housings

Eccentric Shafts

Rebuilt Machines

Ducts

Sprockets

Rubber Gum Balls

Fiberglass

Wilmot Penn Reels

Elevator Buckets

Space for several product photos (we’ve uploaded images)

Clean industrial aesthetic

Back of brochure:

More detailed visual layout of products

Strong callout section showing companies we represent (logos included)

Optional short paragraph about Tovrik’s capabilities, history, or differentiators

Contact info section

Overall style:

Clean, modern, print-ready

Industrial yet polished

Balanced visual + text layout

Color palette aligned with Tovrik brand

Final files delivered as print-ready PDF (plus editable source file if available)

We’ve uploaded product imagery, partner logos, and reference materials. Please design multiple layout concepts if possible.

```html
<!DOCTYPE html>
<html lang="en">
<head>
<meta charset="utf-8">
<title>Tovrik Brochure</title>
<link href="https://fonts.googleapis.com/css2?family=Roboto:wght@400;500;700;900&display=swap" rel="stylesheet">
<style>
:root{
  --blue:#12388f;
  --gold:#d2b57f;
  --tan:#d5b985;
  --ink:#1b1b1b;
  --bg:#dcdde0;
  --white:#ffffff;
}
*{margin:0;padding:0;box-sizing:border-box}
html,body{width:1200px;height:832px;overflow:hidden;background:var(--bg);font-family:'Roboto',sans-serif;color:var(--ink)}
.canvas{position:relative;width:1200px;height:832px}
.page{position:absolute;top:36px;width:537px;height:759px;background:var(--white);overflow:hidden}
.page.front{left:44px}
.page.back{left:618px;border-top:4px solid var(--blue)}
/* front hero */
.hero{position:absolute;left:0;top:0;width:537px;height:250px;background:radial-gradient(ellipse at 30% 40%,#6b5644 0%,#3e3027 45%,#1f1914 100%)}
.hero-curve{position:absolute;left:0;top:0}
.brand{position:absolute;top:28px;width:100%;text-align:center;color:var(--white);font-weight:900;font-size:28px;letter-spacing:2px}
.kicker{position:absolute;top:79px;width:100%;text-align:center;color:var(--white);font-size:13px;font-weight:500}
.headline{position:absolute;top:98px;width:100%;text-align:center;color:var(--white);font-size:27px;font-weight:700;line-height:28px}
.product{position:absolute}
.product .photo{width:100%;border-radius:4px;box-shadow:0 1px 3px rgba(0,0,0,.3)}
.product .label{text-align:center;font-size:12.5px;margin-top:12px;line-height:13px}
.product.small .label{font-size:10.5px;margin-top:10px;line-height:12.5px}
/* footer */
.footer{position:absolute;left:0;bottom:0;width:537px;height:36px;background:var(--blue);display:flex;align-items:center;padding-left:86px;gap:14px;color:var(--white);font-size:8.6px}
.footer .item{display:flex;align-items:center;gap:7px;white-space:nowrap}
.footer .ic{width:19px;height:19px;border-radius:50%;background:var(--gold);display:flex;align-items:center;justify-content:center}
.mark-box{position:absolute;left:27px;bottom:0;width:41px;height:40px;background:var(--white);display:flex;align-items:center;justify-content:center}
.mark-box span{width:26px;height:26px;border-radius:50%;background:var(--blue)}
/* back */
.section-title{position:absolute;top:20px;width:100%;text-align:center;font-size:24px;font-weight:900;letter-spacing:.5px}
.title-rule{position:absolute;top:51px;left:250px;width:37px;height:2px;background:var(--blue)}
.cat{position:absolute;width:100px}
.tag{height:24px;color:var(--white);font-weight:700;font-size:11px;display:flex;align-items:center;padding-left:11px;clip-path:polygon(0 0,90% 0,100% 100%,0 100%)}
.tag.blue{background:var(--blue)}
.tag.gold{background:var(--gold)}
.cat p{font-size:7.4px;line-height:10.8px;margin-top:10px;padding-left:1px;width:104px}
.cat.sm{width:86px}
.cat.sm .tag{height:20px;font-size:9px;padding-left:9px}
.cat.sm p{font-size:5.6px;line-height:8.8px;margin-top:8px;width:86px}
.about{position:absolute;left:0;top:364px;width:268px;height:258px;background:var(--tan);padding:26px 24px 0 27px;color:var(--white)}
.services{position:absolute;left:268px;top:364px;width:269px;height:258px;background:var(--blue);padding:26px 20px 0 22px;color:var(--white)}
.block-title{font-size:18px;font-weight:700}
.block-rule{width:37px;height:2px;background:var(--white);margin:6px 0 12px}
.about .lead{font-size:8.4px;font-weight:700;line-height:13.8px}
.about .body{font-size:8px;line-height:14px;margin-top:15px}
.services .body{font-size:6.6px;line-height:12.6px}
.svc-grid{display:grid;grid-template-columns:108px 108px;row-gap:18px;margin-top:13px}
.svc{display:flex;align-items:center;gap:6px;font-size:7px;font-weight:500;line-height:11px}
.svc .ic{width:18px;height:18px;border-radius:50%;background:var(--white);flex:none;display:flex;align-items:center;justify-content:center}
.partners{position:absolute;top:656px;left:26px;width:485px;display:flex;justify-content:space-between}
.partners span{width:90px;height:28px;border-radius:4px;background:#cfd1d6}
</style>
</head>
<body>
<div class="canvas">

  <!-- FRONT -->
  <section class="page front">
    <div class="hero" role="img" aria-label="Workshop photo of a worker grinding metal with sparks flying"></div>
    <svg class="hero-curve" width="537" height="260" viewBox="0 0 537 260">
      <path d="M0,178 Q268,272 537,178 L537,260 L0,260 Z" fill="#ffffff"/>
      <path d="M34,194 Q268,264 503,194 Q268,246 34,194 Z" fill="#12388f"/>
    </svg>
    <div class="brand">TOVRIK</div>
    <div class="kicker">We Manufacture &amp; Supply</div>
    <h1 class="headline">Replacement Parts for<br>Peanut Processing Equipment</h1>

    <div class="product" style="left:27px;top:268px;width:115px">
      <div class="photo" style="height:115px;background:linear-gradient(135deg,#d5d7d9,#8a8d90)" role="img" aria-label="Perforated flat screens"></div>
      <div class="label">Flat Screens</div></div>
    <div class="product" style="left:150px;top:268px;width:115px">
      <div class="photo" style="height:115px;background:linear-gradient(135deg,#bfc0bd,#5b5c58)" role="img" aria-label="Sheller grates"></div>
      <div class="label">Sheller Grates</div></div>
    <div class="product" style="left:273px;top:268px;width:115px">
      <div class="photo" style="height:115px;background:linear-gradient(135deg,#a7a8a6,#4f504e)" role="img" aria-label="Ripple screens"></div>
      <div class="label">Ripple Screens</div></div>
    <div class="product" style="left:396px;top:268px;width:115px">
      <div class="photo" style="height:115px;background:linear-gradient(135deg,#b9b3a3,#5e5a50)" role="img" aria-label="Stacked sheller bars"></div>
      <div class="label">Sheller Bars</div></div>

    <div class="product" style="left:27px;top:424px;width:115px">
      <div class="photo" style="height:115px;background:linear-gradient(135deg,#a49c8c,#5b5346)" role="img" aria-label="Eccentric shafts"></div>
      <div class="label">Eccentric Shafts</div></div>
    <div class="product" style="left:150px;top:424px;width:115px">
      <div class="photo" style="height:115px;background:linear-gradient(135deg,#a7a79a,#55564d)" role="img" aria-label="Forklift moving a rebuilt machine"></div>
      <div class="label">Rebuilt Machines</div></div>
    <div class="product" style="left:273px;top:424px;width:115px">
      <div class="photo" style="height:115px;background:linear-gradient(135deg,#b8ab93,#6b5f4c)" role="img" aria-label="Rolled duct material"></div>
      <div class="label">Ducts</div></div>
    <div class="product" style="left:396px;top:424px;width:115px">
      <div class="photo" style="height:115px;background:linear-gradient(135deg,#6c6e70,#2c2d2f)" role="img" aria-label="Stacked sprockets"></div>
      <div class="label">Sprockets</div></div>

    <div class="product small" style="left:27px;top:582px;width:90px">
      <div class="photo" style="height:89px;background:linear-gradient(135deg,#9e9a92,#4f4b45)" role="img" aria-label="Eccentric bearing housing"></div>
      <div class="label">Eccentric Bearing<br>Housings</div></div>
    <div class="product small" style="left:125px;top:582px;width:90px">
      <div class="photo" style="height:89px;background:linear-gradient(135deg,#ded7c4,#9d9580)" role="img" aria-label="Rubber gum balls"></div>
      <div class="label">Rubber Gum Balls</div></div>
    <div class="product small" style="left:223px;top:582px;width:90px">
      <div class="photo" style="height:89px;background:linear-gradient(135deg,#b7b2a8,#6d685f)" role="img" aria-label="Worker fitting fiberglass parts"></div>
      <div class="label">Fiberglass</div></div>
    <div class="product small" style="left:322px;top:582px;width:90px">
      <div class="photo" style="height:89px;background:linear-gradient(135deg,#8c8d84,#44453f)" role="img" aria-label="Reel hub part"></div>
      <div class="label">Wilmot Penn Reels</div></div>
    <div class="product small" style="left:420px;top:582px;width:90px">
      <div class="photo" style="height:89px;background:linear-gradient(135deg,#8f9296,#3f4249)" role="img" aria-label="Rows of elevator buckets"></div>
      <div class="label">Elevator Buckets</div></div>

    <div class="footer">
      <div class="item"><span class="ic"><svg width="9" height="11" viewBox="0 0 9 11"><path d="M4.5,0C2,0 0,2 0,4.4C0,7.5 4.5,11 4.5,11S9,7.5 9,4.4C9,2 7,0 4.5,0Z" fill="#fff"/><circle cx="4.5" cy="4.4" r="1.6" fill="#d2b57f"/></svg></span>118 Mill Road Ashford Bend, GA 31700</div>
      <div class="item"><span class="ic"><svg width="10" height="7" viewBox="0 0 10 7"><rect width="10" height="7" rx="1" fill="#fff"/><path d="M0.5,0.5L5,4L9.5,0.5" stroke="#d2b57f" fill="none"/></svg></span>sales@tovrikinc.com</div>
      <div class="item"><span class="ic"><svg width="9" height="9" viewBox="0 0 9 9"><path d="M2,0L3.5,2.5L2.5,3.6Q3.5,5.6 5.4,6.5L6.5,5.5L9,7L8,9Q3,8.7 0,1Z" fill="#fff"/></svg></span>(555) 014-2230</div>
    </div>
    <div class="mark-box"><span></span></div>
  </section>

  <!-- BACK -->
  <section class="page back">
    <h2 class="section-title">PRODUCT CATEGORY</h2>
    <div class="title-rule"></div>

    <div class="cat" style="left:26px;top:70px"><div class="tag blue">Flat Screens</div><p>Lorem ipsum dolor sit amet, consectetur adipiscing elit, sed do eiusmod tempor incididunt ut labore et dolore aliqua.</p></div>
    <div class="cat" style="left:153px;top:70px"><div class="tag gold">Sheller Grates</div><p>Lorem ipsum dolor sit amet, consectetur adipiscing elit, sed do eiusmod tempor incididunt ut labore et dolore aliqua.</p></div>
    <div class="cat" style="left:280px;top:70px"><div class="tag blue">Ripple Screens</div><p>Lorem ipsum dolor sit amet, consectetur adipiscing elit, sed do eiusmod tempor incididunt ut labore et dolore aliqua.</p></div>
    <div class="cat" style="left:407px;top:70px"><div class="tag gold">Sheller Bars</div><p>Lorem ipsum dolor sit amet, consectetur adipiscing elit, sed do eiusmod tempor incididunt ut labore et dolore aliqua.</p></div>

    <div class="cat" style="left:26px;top:166px;width:106px"><div class="tag blue">Eccentric Bearing</div><p>Lorem ipsum dolor sit amet, consectetur adipiscing elit, sed do eiusmod tempor incididunt ut labore et dolore aliqua.</p></div>
    <div class="cat" style="left:153px;top:166px;width:106px"><div class="tag gold">Eccentric Shafts</div><p>Lorem ipsum dolor sit amet, consectetur adipiscing elit, sed do eiusmod tempor incididunt ut labore et dolore aliqua.</p></div>
    <div class="cat" style="left:280px;top:166px;width:110px"><div class="tag blue">Rebuilt Machines</div><p>Lorem ipsum dolor sit amet, consectetur adipiscing elit, sed do eiusmod tempor incididunt ut labore et dolore aliqua.</p></div>
    <div class="cat" style="left:407px;top:166px"><div class="tag gold">Ducts</div><p>Lorem ipsum dolor sit amet, consectetur adipiscing elit, sed do eiusmod tempor incididunt ut labore et dolore aliqua.</p></div>

    <div class="cat sm" style="left:27px;top:272px"><div class="tag blue">Sprockets</div><p>Lorem ipsum dolor sit amet, consectetur adipiscing elit, sed do eiusmod tempor incididunt ut labore et dolore aliqua.</p></div>
    <div class="cat sm" style="left:126px;top:272px;width:90px"><div class="tag gold">Rubber Gum Balls</div><p>Lorem ipsum dolor sit amet, consectetur adipiscing elit, sed do eiusmod tempor incididunt ut labore et dolore aliqua.</p></div>
    <div class="cat sm" style="left:224px;top:272px"><div class="tag blue">Fiberglass</div><p>Lorem ipsum dolor sit amet, consectetur adipiscing elit, sed do eiusmod tempor incididunt ut labore et dolore aliqua.</p></div>
    <div class="cat sm" style="left:325px;top:272px;width:92px"><div class="tag gold">Wilmot Penn Reels</div><p>Lorem ipsum dolor sit amet, consectetur adipiscing elit, sed do eiusmod tempor incididunt ut labore et dolore aliqua.</p></div>
    <div class="cat sm" style="left:422px;top:272px;width:90px"><div class="tag blue">Elevator Buckets</div><p>Lorem ipsum dolor sit amet, consectetur adipiscing elit, sed do eiusmod tempor incididunt ut labore et dolore aliqua.</p></div>

    <div class="about">
      <h3 class="block-title">About Tovrik’s</h3>
      <div class="block-rule"></div>
      <p class="lead">We believe in simple small town values like hard work, community and quality. That’s why you’ll find our team working day in and day out to provide our customers with quality products.</p>
      <p class="body">Our replacement parts are designed and manufactured in our fabrication facility in Ashford Bend, GA. With our American made parts, you can be assured of quality, availability and on-time delivery. Our parts are fabricated to exact customer specifications. Plus, unlike large corporations and foreign manufactures, we are easy to reach if you need to talk to someone.</p>
    </div>

    <div class="services">
      <h3 class="block-title">Our Services</h3>
      <div class="block-rule"></div>
      <p class="body">At TOVRIK, Inc., we manufacture and distribute replacement parts for peanut processing equipment. American-made, high-quality parts that are designed to work great in your equipment. We have been producing, reliable products at our facility Ashford Bend, Georgia since 1996.</p>
      <div class="svc-grid">
        <div class="svc"><span class="ic"><svg width="10" height="10" viewBox="0 0 10 10"><circle cx="5" cy="5" r="3.5" fill="none" stroke="#12388f" stroke-width="1.4"/></svg></span>Equipment<br>Manufacturing</div>
        <div class="svc"><span class="ic"><svg width="10" height="10" viewBox="0 0 10 10"><rect x="1.5" y="1.5" width="7" height="7" fill="none" stroke="#12388f" stroke-width="1.4"/></svg></span>Replacement Parts<br>Manufacturing</div>
        <div class="svc"><span class="ic"><svg width="10" height="10" viewBox="0 0 10 10"><path d="M1,5H9M5,1V9" stroke="#12388f" stroke-width="1.4"/></svg></span>Replacement Parts<br>Distribution</div>
        <div class="svc"><span class="ic"><svg width="10" height="10" viewBox="0 0 10 10"><path d="M1,9H9M2.5,9V4L5,1.5L7.5,4V9" fill="none" stroke="#12388f" stroke-width="1.3"/></svg></span>Welding &amp;<br>Fabrication</div>
        <div class="svc"><span class="ic"><svg width="10" height="10" viewBox="0 0 10 10"><path d="M1.5,5L4,7.5L8.5,2.5" fill="none" stroke="#12388f" stroke-width="1.5"/></svg></span>Sheller Equipment<br>Refurbishing</div>
        <div class="svc"><span class="ic"><svg width="10" height="10" viewBox="0 0 10 10"><path d="M2,6V5A3,3 0 0 1 8,5V6" fill="none" stroke="#12388f" stroke-width="1.3"/><rect x="1.3" y="5.5" width="1.8" height="2.5" fill="#12388f"/><rect x="6.9" y="5.5" width="1.8" height="2.5" fill="#12388f"/></svg></span>Customer<br>Support</div>
      </div>
    </div>

    <div class="partners">
      <span role="img" aria-label="Partner badge"></span>
      <span role="img" aria-label="Partner badge"></span>
      <span role="img" aria-label="Partner badge"></span>
      <span role="img" aria-label="Partner badge"></span>
    </div>

    <div class="footer">
      <div class="item"><span class="ic"><svg width="9" height="11" viewBox="0 0 9 11"><path d="M4.5,0C2,0 0,2 0,4.4C0,7.5 4.5,11 4.5,11S9,7.5 9,4.4C9,2 7,0 4.5,0Z" fill="#fff"/><circle cx="4.5" cy="4.4" r="1.6" fill="#d2b57f"/></svg></span>118 Mill Road Ashford Bend, GA 31700</div>
      <div class="item"><span class="ic"><svg width="10" height="7" viewBox="0 0 10 7"><rect width="10" height="7" rx="1" fill="#fff"/><path d="M0.5,0.5L5,4L9.5,0.5" stroke="#d2b57f" fill="none"/></svg></span>sales@tovrikinc.com</div>
      <div class="item"><span class="ic"><svg width="9" height="9" viewBox="0 0 9 9"><path d="M2,0L3.5,2.5L2.5,3.6Q3.5,5.6 5.4,6.5L6.5,5.5L9,7L8,9Q3,8.7 0,1Z" fill="#fff"/></svg></span>(555) 014-2230</div>
    </div>
    <div class="mark-box"><span></span></div>
  </section>

</div>
</body>
</html>
```